Training Course Info Brochure

Hi there, I'm looking for a design for A4 Flyer (2-3 pages) on our new Course - Infection Control. I have included a previous brochure on our courses so the designed can see the look and feel we are looking for.

As this is about Infection Control, I would also like to see some RED in the design or wording.

The brochure will need to include quite a few industry/ government logos as well and graphics are important. I have included some (Health Care Industry workers) and am also open to other graphics.

Thanks for considering!

Target Market(s)

The Health profession and students wanting to work in the health field

Industry/Entity Type

Health Care

Font styles to use
Sans Serif

Colors
3277b5
f78f20
ffffff
ec1f27

Requirements
Must have
• Similar feel to the brochure I have included in this brief.

SOME RED lettering as we are teaching Infection Control during the COVID19 pandemic
Nice to have
• Lovely design with quite a few photos graphics

Company details:

Harcourt Academy of Learning
RTO 73846
FREECALL : 1800 472 913
www.brindlewoodtraining.edu.au
info@harcourtlearning.edu.au

```html
<!DOCTYPE html>
<html lang="en">
<head>
<meta charset="utf-8">
<title>Infection Control Course Brochure – Page 01</title>
<link href="https://fonts.googleapis.com/css2?family=Arimo:wght@700&family=Carlito:wght@400;700&family=Open+Sans:wght@600;700&family=Roboto+Condensed:wght@400;700&display=swap" rel="stylesheet">
<style>
  :root {
    --red: #dc252d;
    --blue: #2b78bd;
    --white: #ffffff;
    --ink: #2a2a2a;
    --frame: #1c1c1c;
    --backdrop: #ffffff;
  }
  * { margin: 0; padding: 0; box-sizing: border-box; }
  html, body { width: 1200px; height: 1200px; overflow: hidden; background: var(--backdrop); }
  .canvas { position: relative; width: 1200px; height: 1200px; }

  .page {
    position: absolute; left: 264px; top: 124px; width: 668px; height: 960px;
    background: var(--red); border: 1px solid var(--frame); overflow: hidden;
  }
  .top-band { position: absolute; left: 0; top: 0; width: 100%; height: 68px; background: var(--red); }
  .hero-photo {
    position: absolute; left: 0; top: 68px; width: 100%; height: 387px;
    background: linear-gradient(100deg, #6f8aa6 0%, #b9c7d6 25%, #5d7592 45%, #2c3c5c 60%, #9fb1c4 80%, #d8e0e8 100%);
  }
  .badge-icon { position: absolute; left: 24px; top: 2px; width: 104px; height: 104px; }

  .unit-title {
    position: absolute; left: 42px; top: 468px; white-space: nowrap;
    font-family: "Open Sans", sans-serif; font-weight: 600; font-size: 14.2px; color: var(--white);
  }

  .content-panel {
    position: absolute; left: 72px; top: 505px; width: 596px; height: 405px; background: var(--white);
  }
  .cost-heading {
    position: absolute; left: 29px; top: 6px; line-height: 1.1;
    font-family: "Carlito", sans-serif; font-weight: 700; font-size: 40px; color: var(--red);
  }
  .cost-band {
    position: absolute; left: 0; top: 56px; width: 595px; height: 60px; background: var(--blue);
    padding: 3px 0 0 29px; white-space: nowrap;
    font-family: "Carlito", sans-serif; font-size: 23.4px; line-height: 28px; color: var(--white);
  }
  .cost-band strong { font-weight: 700; }
  .about-heading {
    position: absolute; left: 33px; top: 120px; white-space: nowrap;
    font-family: "Arimo", sans-serif; font-weight: 700; font-size: 33.5px; color: var(--red); line-height: 1;
  }
  .about-tagline {
    position: absolute; left: 35px; top: 156px; white-space: nowrap;
    font-family: "Roboto Condensed", sans-serif; font-weight: 700; font-size: 11.4px; color: var(--red);
  }
  .about-body {
    position: absolute; left: 35px; top: 182px; width: 516px;
    font-family: "Roboto Condensed", sans-serif; font-size: 11.2px; line-height: 13.8px; color: var(--ink);
    text-align: justify; hyphens: auto;
  }
  .about-body p { margin-bottom: 14px; }
  .about-body strong { font-weight: 700; }
  .about-body .accent { color: var(--red); font-weight: 700; }

  .page-number {
    position: absolute; left: 0; top: 924px; width: 59px; height: 36px; background: var(--blue);
    font-family: "Open Sans", sans-serif; font-weight: 600; font-size: 18px; color: var(--white);
    text-align: center; line-height: 34px;
  }
  .site-url {
    position: absolute; left: 59px; right: 0; top: 922px; text-align: center; padding-left: 20px;
    font-family: "Open Sans", sans-serif; font-weight: 600; font-size: 18px; color: var(--white);
  }
</style>
</head>
<body>
<div class="canvas">
  <section class="page">
    <div class="top-band"></div>
    <div class="hero-photo" role="img" aria-label="Photo of a worker in a mask and gloves wiping down a stainless steel lift interior"></div>
    <svg class="badge-icon" viewBox="0 0 104 104" role="img" aria-label="Virus icon">
      <circle cx="52" cy="52" r="50" fill="var(--red)" stroke="#f3b7ba" stroke-width="3"/>
    </svg>

    <h2 class="unit-title">HLTINF001 -Comply with infection prevention and control policies and procedures-</h2>

    <div class="content-panel">
      <h1 class="cost-heading">Course Cost</h1>
      <div class="cost-band">Free infection control skill sets for everyone in<br>Western&nbsp; Australia or <strong>$350/for students outside of WA.</strong></div>

      <h2 class="about-heading">About This Course</h2>
      <p class="about-tagline">Protect yourself and others in the community from infectious diseases</p>
      <div class="about-body">
        <p>There is not better time than now, to formally Upskill yourself and your team with a Nationally Accredited unit of Competen&shy;cy in Infection Control prevention <strong>including the latest COVID19 infection control protocols</strong> (Department of Health). Fast track your skills with Brindlewood’s Accredited Infection Control Skill set to get you job ready or enhance your current workplace skills. The COVID19 pandemic has highlighted the important of building the capacity and understanding of the workforce to <span class="accent">practice safe infection control procedures.</span></p>
        <p>This skill set will provide you with the skills and knowledge to assist in protecting yourself and others in the community from infectious diseases.</p>
        <p>You will understand how infections are spread, ways of preventing the spread of infection and how to protect yourself and others from infection.</p>
        <p>The skill set is becoming increasingly important for all Health Care Workers -and all workers are encouraged to upskill themselves today, whether you are becoming Job Ready or for your professional development in Industry.</p>
      </div>
    </div>

    <div class="page-number">01</div>
    <div class="site-url">www.brindlewoodtraining.edu.au</div>
  </section>
</div>
</body>
</html>
```